Branding Postcard for Real Estate Brokerage

I am a Real Estate Broker looking for a template postcard that I can use with lots of types of situations , solds, listed property, etc but has a standard layout that is consistent so it will be recognizable and tied to me. There was one that was on the template group that caught my eye. I was thinking of using the A in my logo as the script or watermark. I have uploaded my idea on that as well as other logos, etc. My goal is to have a template that I can add text to and market different things / sales / request action for pricing, etc.

Target Market(s)

Homeowners in Neighborhoods where I have sold homes

Industry/Entity Type

Real Estate

Requirements
Must have
• Area to add label for mailing, Area in front has to be a template where I can write specifics of the mailing, Consistent branding

```html
<!DOCTYPE html>
<html lang="en">
<head>
<meta charset="utf-8">
<title>Just Sold Postcard – Harborline Realty Group</title>
<link rel="stylesheet" href="https://fonts.googleapis.com/css2?family=Carlito:wght@400&family=Arimo:wght@400&display=swap">
<style>
  :root {
    --brand-purple: #3d2577;
    --headline-grey: #d9d7dc;
    --watermark: #e6e2ef;
    --ink: #111111;
    --paper: #ffffff;
  }
  * { margin: 0; padding: 0; box-sizing: border-box; }
  html, body {
    width: 1200px;
    height: 930px;
    overflow: hidden;
    background: var(--paper);
  }
  .postcard {
    position: relative;
    width: 1200px;
    height: 930px;
    background: var(--paper);
    font-family: "Carlito", sans-serif;
  }
  .brand-watermark {
    position: absolute;
    left: 70px;
    top: 440px;
    font-family: "Carlito", sans-serif;
    font-size: 130px;
    line-height: 1;
    color: var(--watermark);
    white-space: nowrap;
  }
  .header-band {
    position: absolute;
    left: 28px;
    top: 69px;
    width: 1144px;
    height: 155px;
    background: var(--brand-purple);
  }
  .headline {
    position: absolute;
    left: 74px;
    top: 104px;
    font-family: "Carlito", sans-serif;
    font-weight: 400;
    font-size: 70px;
    line-height: 1;
    color: var(--headline-grey);
  }
  .offer-label {
    position: absolute;
    left: 91px;
    top: 305px;
    font-family: "Arimo", sans-serif;
    font-size: 29px;
    line-height: 1;
    letter-spacing: -0.5px;
    color: var(--ink);
  }
  .property-photo {
    position: absolute;
    left: 703px;
    width: 430px;
  }
  .property-photo--featured {
    top: 271px;
    height: 268px;
    background:
      radial-gradient(ellipse 55% 30% at 45% 52%, rgba(138,118,88,0.85), rgba(138,118,88,0) 100%),
      linear-gradient(180deg, #3f79c4 0%, #7fa6d6 30%, #9a9172 50%, #6e8f3e 70%, #5b8a2f 100%);
  }
  .property-photo--secondary {
    top: 582px;
    height: 229px;
    background:
      radial-gradient(ellipse 45% 40% at 48% 55%, rgba(236,238,236,1), rgba(236,238,236,0) 100%),
      linear-gradient(180deg, #d6e6ec 0%, #a9c795 30%, #7fa86a 60%, #6c786c 88%, #55605a 100%);
  }
  .brokerage {
    position: absolute;
    left: 79px;
    top: 712px;
    color: var(--ink);
  }
  .brokerage-name {
    font-size: 32px;
    line-height: 1;
    font-variant: small-caps;
  }
  .brokerage-phone {
    margin-top: 12px;
    font-size: 37px;
    line-height: 1;
    letter-spacing: 1px;
  }
  .footer-band {
    position: absolute;
    left: 31px;
    top: 851px;
    width: 1141px;
    height: 50px;
    background: var(--brand-purple);
  }
</style>
</head>
<body>
  <main class="postcard">
    <div class="brand-watermark" aria-hidden="true">Harborline</div>

    <header class="header-band"></header>
    <h1 class="headline">JUST SOLD</h1>

    <p class="offer-label">SPECIAL OFFERS</p>

    <div class="property-photo property-photo--featured" role="img" aria-label="Photo of a two-storey stone and shingle family home with landscaped front garden and curved walkway under a blue sky"></div>
    <div class="property-photo property-photo--secondary" role="img" aria-label="Photo of a white two-storey house with dark red roof, covered carport and surrounding trees"></div>

    <div class="brokerage">
      <p class="brokerage-name">Harborline Realty Group</p>
      <p class="brokerage-phone">312-555-0148</p>
    </div>

    <footer class="footer-band"></footer>
  </main>
</body>
</html>
```